Bold Cover needed for a book on Workplace Bullying

I need a book cover design for a book titled, “Iron Silence?” The book recounts my story of bullying in the workplace. It also includes chapters on how readers can minimize/stop workplace bullying, write an effective complaint, and ensure their own mental wellbeing.
I am looking for a bold design using red and black, and possibly distressed lettering. The covers of other books dealing with this subject do not reflect my vision. They are often too childish or look too academic. This book needs to stress the serious nature of a toxic workplace, while appealing to readers experiencing a similar situation. I’d like the cover to reflect the mental anguish associated with workplace bullying (hence the distressed lettering).
I have included a cover that appeals to me (although the coloring is wrong). That said, I am also very happy (and excited) to see your creative input!
On the cover, it should have the following:
Title: Iron Silence?
Subtitle: How the Harbour Works Department Condones Bullying & Ruins Lives
Author: Owen Frick
Other relevant details:
Book size: 5.5” x 8.5”
Back cover will have a blurb, author picture/short bio, and barcode
The blurb on the back cover reads:
Undermining, intimidation and threats
Despite the Department of Harbour Works allegedly holding a Iron Silence? for bullying, these behaviours were an everyday occurrence in at least one workplace. Even after a decade of complaints, numerous witnesses and physical proof, the department failed to act. Instead, they looked the other way, allowing one powerful and well-connected individual to end careers and ruin lives.
After being targeted, one teacher resolved to put an end to the abuse experienced by more than fifty employees. His startling story reveals the relentless bullying, mental health ramifications, and insidious tactics used to cover up the corrosive behaviour.
Those who have experienced a toxic workplace will also find much needed support and guidance, intended to minimise suffering and detail a clear way forward. Chapters include dealing with bullying in the workplace, how to lodge a successful complaint, and how to stay sane during any potential legal action.

```html
<!DOCTYPE html>
<html lang="en">
<head>
<meta charset="utf-8">
<title>Iron Silence? — Owen Frick</title>
<link rel="stylesheet" href="https://fonts.googleapis.com/css2?family=Montserrat:wght@800;900&family=Oswald:wght@500&display=swap">
<style>
  :root {
    --ink: #000000;
    --paper: #ffffff;
    --alarm-red: #d62728;
  }
  html, body {
    margin: 0;
    padding: 0;
    width: 825px;
    height: 1200px;
    overflow: hidden;
    background: var(--ink);
  }
  .cover {
    display: block;
    width: 825px;
    height: 1200px;
    background: var(--ink);
  }
  .author-name {
    font-family: "Montserrat", sans-serif;
    font-weight: 900;
    font-size: 26px;
    letter-spacing: 1px;
    fill: var(--paper);
  }
  .title-letter {
    font-family: "Montserrat", sans-serif;
    font-weight: 900;
    font-size: 450px;
    fill: var(--paper);
  }
  .title-second-word {
    font-family: "Montserrat", sans-serif;
    font-weight: 900;
    font-size: 96px;
    fill: var(--paper);
  }
  .title-ring {
    fill: none;
    stroke: var(--alarm-red);
    stroke-width: 78;
  }
  .subtitle {
    font-family: "Oswald", sans-serif;
    font-weight: 500;
    font-size: 15px;
    letter-spacing: 0.3px;
    fill: var(--paper);
    text-anchor: middle;
  }
</style>
</head>
<body>
<svg class="cover" viewBox="0 0 825 1200" xmlns="http://www.w3.org/2000/svg" role="img" aria-label="Iron Silence? — How the Harbour Works Department Condones Bullying &amp; Ruins Lives, by Owen Frick">
  <text class="author-name" x="25" y="200">OWEN FRICK</text>

  <g class="title-main">
    <text class="title-letter" x="8" y="548">I</text>
    <text class="title-letter" x="182" y="548">R</text>
    <circle class="title-ring" cx="166" cy="728" r="126"/>
    <text class="title-letter" x="350" y="893">N</text>
  </g>

  <g class="subtitle-block" transform="rotate(-48 166 728)">
    <text class="subtitle" x="166" y="690">HOW</text>
    <text class="subtitle" x="166" y="712">THE HARBOUR WORKS</text>
    <text class="subtitle" x="166" y="734">DEPARTMENT CONDONES</text>
    <text class="subtitle" x="166" y="756">BULLYING &amp; RUINS</text>
    <text class="subtitle" x="166" y="778">LIVES</text>
  </g>

  <text class="title-second-word" x="0" y="975">SILENCE?</text>
</svg>
</body>
</html>
```